Verdano Harvest - Stationery Design Project

We need a stationary for our business. We grow roots and fruits in Central and South America, we import and distribute in FL, USA. We do fresh and frozen products.

Target Market(s)

Small and big supermarkets, wholesalers, traders, distributors, etc

Industry/Entity Type

Business

```html
<!DOCTYPE html>
<html lang="en">
<head>
<meta charset="utf-8">
<title>Verdano Harvest – Stationery</title>
<link rel="stylesheet" href="https://fonts.googleapis.com/css2?family=Questrial&display=swap">
<style>
  :root{
    --backdrop:#e6eaec;
    --paper:#ffffff;
    --paper-back:#f1f1f1;
    --ink:#3d3d3d;
    --ink-dark:#2b2b2b;
    --orange:#e8820c;
    --olive:#566a2c;
    --rule:#8a8a8a;
  }
  *{margin:0;padding:0;box-sizing:border-box}
  html,body{width:1200px;height:927px;overflow:hidden}
  body{background:var(--backdrop);font-family:"Questrial",sans-serif;color:var(--ink);position:relative}

  .sheet{position:absolute;top:45px;width:511px;height:696px;border-radius:14px;overflow:hidden;
    box-shadow:0 2px 6px rgba(0,0,0,.18)}
  .sheet--front{left:43px;background:var(--paper)}
  .sheet--back{left:635px;background:var(--paper-back)}

  .brand{position:absolute;font-size:22px;letter-spacing:.5px;color:var(--orange);display:flex;align-items:center;gap:8px;white-space:nowrap}
  .brand__dot{width:12px;height:12px;border-radius:50%;background:currentColor}
  .sheet--front .brand{left:47px;top:50px}
  .sheet--back .brand{left:0;right:0;justify-content:center;top:602px;font-size:26px;color:var(--olive)}

  .contact{position:absolute;right:39px;top:41px;text-align:right;font-size:8.6px;line-height:13px;color:#7a7a7a}
  .contact b{color:var(--orange);font-weight:400}
  .contact__rule{position:absolute;left:237px;right:39px;top:79px;height:2px;background:var(--rule)}
  .contact__address{position:absolute;right:39px;top:83px;font-size:8.4px;color:var(--ink-dark);font-weight:700;letter-spacing:.1px}

  .letter{position:absolute;left:44px;top:143px;width:425px;font-size:10.3px;line-height:15.6px;text-align:justify;hyphens:auto;color:var(--ink)}
  .letter p+p{margin-top:15.6px}

  .signature{position:absolute;left:380px;top:583px}
  .signature__name{font-size:13px;color:var(--ink-dark)}
  .signature__role{font-size:9px;margin-top:7px;color:var(--ink)}

  .footer-band{position:absolute;left:0;right:0;bottom:0;height:38px;background:var(--orange);
    display:flex;align-items:center;justify-content:center;color:#fff;font-size:9.5px;font-weight:700;letter-spacing:1.6px}
</style>
</head>
<body>
  <section class="sheet sheet--front" aria-label="Letterhead front">
    <div class="brand"><span>VERDANO HARVEST</span><span class="brand__dot"></span></div>

    <div class="contact">
      <div><b>Tel:</b> 305.555.0142</div>
      <div><b>Mob:</b> 305.555.0187</div>
      <div><b>Fax:</b> 305.555.0163</div>
    </div>
    <div class="contact__rule"></div>
    <div class="contact__address">1840 Palm Grove Avenue, Miami, FL 33142</div>

    <div class="letter" lang="la">
      <p>Lorem ipsum dolor sit amet, consectetur adipiscing elit. Donec orci purus, luctus vitae dignissim eu, iaculis sed purus. Vivamus faucibus, ipsum nec aliquet viverra, leo mauris condimentum ligula, sit amet sagittis enim ligula quis arcu. Nam egestas tortor id nisi porttitor mattis. In tortor ante, ultricies in suscipit a, tempus non massa. Vivamus et auctor mi. Fusce vel massa nulla. Phasellus nec eros mauris, et scelerisque orci. Donec malesuada orci vitae nulla accumsan porta a id massa.</p>
      <p>Quisque accumsan iaculis magna sit amet fringilla. Maecenas consequat, magna eget tincidunt semper, odio nibh rutrum mi, id feugiat ante nisi eu risus. Vestibulum nunc orci, rhoncus a placerat in, ultricies in mi. Cras mattis varius eros, vel fringilla nisi suscipit eget. Quisque scelerisque sagittis nulla at porttitor. Mauris a justo et tellus interdum tristique. Sed id augue vitae urna euismod commodo aliquet a quam. Pellentesque arcu velit, cursus et malesuada ut, consequat et diam. Nullam erat sem, rhoncus id ullamcorper vitae, rhoncus et arcu. In ultricies ultricies nulla,</p>
      <p>Kut rutrum nisi iaculis at. Donec eu magna a metus ornare faucibus. Fusce aliquet faucibus ultricies. Morbi semper, est id tincidunt gravida, sem arcu adipiscing lacus, ac bibendum nulla leo eu purus. Quisque nec diam sed risus consectetur a ccumsan quis quis nibh. Vestibulum id purus lorem. Donec eu magna a metus ornare faucibus. Fusce aliquet faucibus ultricies. Morbi semper, est id tincidunt gravida, sem arcu adipiscing lacus, ac bibendum nulla leo eu purus. Quisque nec diam sed risus consectetur a ccumsan quis quis nibh. Vestibulum id purus lorem.</p>
    </div>

    <div class="signature">
      <div class="signature__name">Elena Ruiz</div>
      <div class="signature__role">Co-Founder &amp; CEO</div>
    </div>

    <div class="footer-band">www.verdanoharvest.com</div>
  </section>

  <section class="sheet sheet--back" aria-label="Letterhead back">
    <div class="brand"><span>VERDANO HARVEST</span><span class="brand__dot"></span></div>
  </section>
</body>
</html>
```